Software engineering company needs business card

I need a cool business card. Company: Byte Merano Larchwood Ave 41 58213 Dunmere Name: Gerald Hofmann CEO / Managing Director & Owner

Industry/Entity Type

Business

```html
<!DOCTYPE html>
<html lang="en">
<head>
<meta charset="utf-8">
<title>Byte Merano — Business Card</title>
<link rel="stylesheet" href="https://fonts.googleapis.com/css2?family=Orbitron:wght@700&family=Roboto:wght@300&display=swap">
<style>
  :root {
    --page: #e9e6e2;
    --card-front: #232323;
    --card-back: #050505;
    --band-dark: #0c0c0c;
    --band-mid: #2a2a2a;
    --glow: #2b2b2b;
    --green: #8cc63f;
    --grey-text: #8a8a8a;
    --mark-grey: #5b5b5d;
  }
  * { margin: 0; padding: 0; box-sizing: border-box; }
  html, body {
    width: 1200px; height: 1200px; overflow: hidden;
    background: var(--page);
  }
  .canvas { position: relative; width: 1200px; height: 1200px; }

  .card {
    position: absolute; left: 250px; width: 700px; height: 400px;
    border-radius: 6px; overflow: hidden;
    box-shadow: 0 18px 40px rgba(0,0,0,.25);
  }
  .card--front { top: 150px; background: var(--card-front); }
  .card--back  { top: 650px; background: var(--card-back); border-bottom: 4px solid var(--green); }
  .card__art { position: absolute; inset: 0; width: 100%; height: 100%; }

  .brand {
    position: absolute; display: flex; align-items: center; gap: 14px;
    white-space: nowrap;
    font-family: "Orbitron", sans-serif; font-weight: 700; color: var(--green);
    letter-spacing: .04em; text-transform: uppercase;
  }
  .brand__square { flex: none; background: var(--mark-grey); }
  .card--front .brand { left: 50%; top: 58px; transform: translateX(-50%); font-size: 26px; }
  .card--front .brand__square { width: 22px; height: 22px; }
  .card--back .brand { left: 50%; top: 50%; transform: translate(-50%,-50%); font-size: 40px; }
  .card--back .brand__square { width: 34px; height: 34px; }

  .details {
    position: absolute; left: 0; right: 0; top: 150px;
    text-align: center; color: var(--green); white-space: nowrap;
  }
  .details__company, .details__name {
    font-family: "Orbitron", sans-serif; font-weight: 700;
    font-size: 19px; letter-spacing: .06em; text-transform: uppercase;
  }
  .details__address {
    font-family: "Roboto", sans-serif; font-weight: 300;
    font-size: 21px; color: var(--grey-text); margin: 10px 0 22px;
  }
  .details__role-tag {
    font-family: "Roboto", sans-serif; font-weight: 300; font-size: 19px;
    text-transform: none; letter-spacing: 0; margin-left: 10px;
  }
  .details__title {
    font-family: "Roboto", sans-serif; font-weight: 300; font-size: 18px; margin-top: 8px;
  }
</style>
</head>
<body>
<main class="canvas">

  <section class="card card--front" aria-label="Business card front">
    <svg class="card__art" viewBox="0 0 700 400">
      <defs>
        <linearGradient id="band-fade-left" x1="0" y1="0" x2="1" y2="0">
          <stop offset="0" stop-color="var(--band-mid)"/>
          <stop offset="1" stop-color="var(--band-dark)"/>
        </linearGradient>
        <linearGradient id="band-fade-right" x1="1" y1="0" x2="0" y2="0">
          <stop offset="0" stop-color="var(--band-mid)"/>
          <stop offset="1" stop-color="var(--band-dark)"/>
        </linearGradient>
      </defs>
      <path class="edge-band edge-band--left" role="img" aria-label="Dark decorative striped side panel"
            d="M0 0 H70 Q150 200 70 400 H0 Z" fill="url(#band-fade-left)"/>
      <path class="edge-band edge-band--right" role="img" aria-label="Dark decorative striped side panel"
            d="M700 0 H630 Q550 200 630 400 H700 Z" fill="url(#band-fade-right)"/>
    </svg>
    <div class="brand"><span class="brand__square"></span><span class="brand__name">Byte Merano</span></div>
    <div class="details">
      <p class="details__company">Byte Merano Larchwood</p>
      <p class="details__address">Ave 41 58213 Dunmere</p>
      <p class="details__name">Gerald Hofmann<span class="details__role-tag">(CEO)</span></p>
      <p class="details__title">M.D &amp; Owner</p>
    </div>
  </section>

  <section class="card card--back" aria-label="Business card back">
    <svg class="card__art" viewBox="0 0 700 400">
      <defs>
        <radialGradient id="back-glow" cx="50%" cy="50%" r="55%">
          <stop offset="0" stop-color="var(--glow)"/>
          <stop offset="1" stop-color="var(--card-back)"/>
        </radialGradient>
      </defs>
      <rect class="back-glow" role="img" aria-label="Soft dark glow behind the company name, decorative striped background"
            width="700" height="400" fill="url(#back-glow)"/>
    </svg>
    <div class="brand"><span class="brand__square"></span><span class="brand__name">Byte Merano</span></div>
  </section>

</main>
</body>
</html>
```